Vermilion Reel Works Web Design

COMPANY: VERMILION REEL WORKS
LOCATION: SHANGHAI, CHINA
AREA: FILM/TV DRAMA/COMMERCIALS/GAME POST PRODUCTION, SOUND DESIGN, MUSIC, and GAME.
WEB STYLE: SIMPLE, PROFESSIONAL, TRUSTWORTHY

LANGUAGE: ENGLISH, CHINESE. (Same layout, different language)
UPDATE: AFTER PROJECT FINISHED, WE NEED UPDATE BY OURSELVES.

MAIN SUBJECT: 6
1 HOMEPAGE
2 ABOUT US
3 TEAM
4 SERVICES
5 FACILITY
6 CONTACT

add one page of JOB OPPORTUNITIES.

DETAILS
1 HOMEPAGE
SLOGAN: Vermilion Reel Works provides a well-designed working environment which amplifies your team’s ability to reach their creative goals.

Our services include:
 Feature Films
 Music & Scoring
 Commercials
 ADR & Foley
 Sound & Picture Editorial
 Sound Design
 Video Game

2 ABOUT US
Vermilion Reel Works is located in the premiere South-Bund area of Shanghai. Occupying a 5000 square meter Technical Building, Vermilion Reel Works was built by a filmmaker for filmmakers, and is one of the largest, most versatile full-service post-production facilities in China.

Vermilion Reel Works is positioning to be at the forefront of the latest technology. Our goal is to provide a comprehensive solution for the post-production needs of our clients. We offer two fully-equipped dubbing stages (one of which will be certified KESTRON VOXAR PREMIERE), a large variety of both picture and sound editing rooms, impressive Foley and ADR stages, a world-class scoring stage, and complete audio and video transfer services.

We can handle your entire project from editing all the way to the end of the final sound mix; all under one extremely comfortable roof. We fully realize that the true art is in listening to the needs of our clients and making their greatest vision a reality. To this end our creative team's expertise, with a network of sound supervisors, editors and mixers, will deliver the magic you need. Producers and directors will also find our richly appointed guest accommodations to be a comfortable and soothing place to wind up the day. Every aspect of your project will be taken care of by a skilled and dedicated team, in the way that is best suited to you.

3 TEAM
(attachment 01)

4 SERVICES
Sound Mix
ADR
FOLEY
MUSIC
Sound Design
Sound Edit
Picture Edit
for all the Films, TV Drama, Commercials, Video Games, Online Media
(attachment 02, use photo)

5 FACILITY
(attachment 03)

6 CONTACT
(attachment04)
with map

Project Deadline Extended
Reason: Designers work are great, my bosses will spend 1-2 days select one of these web design, and spend 1-2 days to make some change, maybe use new photos.

```html
<!DOCTYPE html>
<html lang="en">
<head>
<meta charset="utf-8">
<title>Vermilion Reel Works</title>
<link href="https://fonts.googleapis.com/css2?family=Roboto:wght@400;500;700&family=Lato:wght@300;400;700&display=swap" rel="stylesheet">
<style>
:root{
  --teal:#2bd4b0;
  --ink:#222;
  --muted:#8a8a8a;
  --dark:#151515;
  --dark-2:#1d1d1d;
  --band:#2a2a2a;
  --white:#fff;
  --amber:#c46a24;
}
*{margin:0;padding:0;box-sizing:border-box}
html,body{width:1200px;height:2315px;overflow:hidden;background:var(--white)}
body{font-family:"Roboto",Arial,sans-serif;color:var(--ink);position:relative}
a{color:inherit;text-decoration:none}

/* header + hero */
.hero{position:absolute;left:0;top:0;width:1200px;height:563px;
  background:radial-gradient(ellipse at 70% 45%,#8a5a2c 0%,#4a2e18 35%,#1d130c 75%,#0e0a07 100%)}
.site-header{position:absolute;left:0;top:0;width:1200px;height:68px;background:rgba(15,12,10,.72);z-index:2}
.brand{position:absolute;left:160px;top:14px;color:var(--white);font-family:"Roboto",sans-serif;font-weight:500;font-size:19px;line-height:40px;letter-spacing:.5px}
.main-nav{position:absolute;left:404px;top:20px;width:574px;display:flex;justify-content:space-between;align-items:center;white-space:nowrap}
.main-nav a{color:var(--white);font-size:11.5px;font-weight:500;letter-spacing:.2px;line-height:26px}
.main-nav a.active{border:1px solid var(--teal);padding:0 10px}
.lang{position:absolute;left:1012px;top:19px;width:28px;height:28px;border-radius:50%;background:var(--amber);color:var(--white);font-size:10px;font-weight:700;text-align:center;line-height:28px}
.hero-copy{position:absolute;left:0;top:148px;width:1200px;text-align:center;color:var(--white)}
.hero-copy svg{display:block;margin:0 auto 14px}
.hero-title{font-size:40px;font-weight:700;letter-spacing:.3px}
.divider{width:80px;height:3px;margin:14px auto 16px;background:var(--white);position:relative}
.divider::after{content:"";position:absolute;left:30px;top:0;width:20px;height:3px;background:var(--teal)}
.hero-sub{font-family:"Lato",sans-serif;font-size:18px;line-height:28px}

/* services grid */
.services{position:absolute;left:160px;top:638px;width:880px;height:450px;display:grid;grid-template-columns:repeat(4,220px);grid-template-rows:repeat(2,225px)}
.service-intro{background:var(--teal);color:var(--white);display:flex;flex-direction:column;align-items:center;justify-content:center}
.service-intro h2{font-family:"Roboto",sans-serif;font-weight:400;font-size:27px}
.service-intro .divider{margin:10px auto 0;width:70px}
.service-intro .divider::after{background:#0f8e73}
.service-card{position:relative;background:linear-gradient(160deg,#5a5a5a,#1c1c1c 70%)}
.service-card:nth-child(3){background:linear-gradient(160deg,#6f6f6f,#262626 70%)}
.service-card:nth-child(4){background:linear-gradient(160deg,#d8d8d8,#6a6a6a 70%)}
.service-card:nth-child(5){background:linear-gradient(160deg,#7a7a82,#202024 70%)}
.service-card:nth-child(6){background:linear-gradient(160deg,#3a3a3a,#111 70%)}
.service-card:nth-child(7){background:linear-gradient(160deg,#8a8a8a,#2a2a2a 70%)}
.service-card:nth-child(8){background:linear-gradient(160deg,#444,#151515 70%)}
.service-card .caption{position:absolute;left:0;bottom:0;width:100%;height:83px;background:rgba(12,12,12,.82);padding:12px 14px 0;color:var(--white)}
.service-card.featured .caption{background:var(--teal)}
.caption h3{font-size:13px;font-weight:500;margin-bottom:8px}
.caption p{font-size:11px;line-height:17px;color:#d8d8d8}
.service-card.featured .caption p{color:var(--white)}

/* studio band */
.studio{position:absolute;left:0;top:1140px;width:1200px;height:468px;background:radial-gradient(ellipse at 40% 50%,#2c2f2a 0%,#161816 60%,#0b0b0b 100%);color:var(--white)}
.studio h2{font-size:21px;font-weight:500;position:absolute;top:56px}
.studio .divider{position:absolute;top:92px;margin:0;width:70px}
.studio .divider::after{left:25px}
.work{position:absolute;left:0;top:0;width:770px}
.work h2{left:268px}
.work .divider{left:343px}
.we-create{position:absolute;left:160px;top:124px;width:450px;text-align:center}
.we-create .kicker{font-size:24px;font-weight:500}
.we-create .big{font-family:"Lato",sans-serif;font-weight:300;font-size:35px;line-height:44px}
.we-create .mid{font-family:"Lato",sans-serif;font-weight:300;font-size:30px;line-height:38px}
.we-create p{font-size:12px;line-height:18px;margin-top:16px;font-weight:500}
.btn{position:absolute;left:300px;top:372px;width:150px;height:38px;background:var(--teal);color:var(--white);font-size:12px;font-weight:500;text-align:center;line-height:38px}
.case h2{left:662px}
.case .divider{left:790px}
.case-media{position:absolute;left:611px;top:113px;width:427px;height:250px;background:radial-gradient(ellipse at 50% 45%,#c9a74a 0%,#7a5a1e 45%,#2a1e0c 100%)}
.case-media svg{position:absolute;left:183px;top:95px}
.case p{position:absolute;left:611px;top:378px;width:430px;font-size:12px;line-height:18px;font-weight:500}

/* blog */
.blog-title{position:absolute;left:0;top:1678px;width:1200px;text-align:center;font-size:26px;font-weight:500}
.blog .divider{position:absolute;top:1717px;left:560px;margin:0;width:80px;background:transparent}
.blog .divider::after{left:28px;width:24px}
.blog-list{position:absolute;left:160px;top:1748px;display:flex;gap:22px}
.post{width:204px}
.post-image{height:133px;position:relative;background:linear-gradient(170deg,#9a8a6a,#2a2a2a 75%)}
.post:nth-child(2) .post-image{background:linear-gradient(170deg,#3c3c3c,#0f0f0f 75%)}
.post:nth-child(3) .post-image{background:linear-gradient(170deg,#b9b2a4,#3a3632 75%)}
.post:nth-child(4) .post-image{background:linear-gradient(170deg,#cfcfcf,#3a3a3a 75%)}
.date{position:absolute;left:12px;top:115px;width:34px;height:38px;background:var(--teal);color:var(--white);text-align:center}
.date b{display:block;font-size:14px;line-height:20px}
.date span{display:block;font-size:9px;line-height:14px}
.post .day{margin:6px 0 0 52px;font-size:11px;color:#555;height:16px}
.post h3{font-size:14px;font-weight:500;margin-top:8px}
.post p{font-size:11px;line-height:17px;color:var(--muted);margin-top:8px}

/* footer */
.footer-contacts{position:absolute;left:0;top:2037px;width:1200px;height:138px;background:linear-gradient(180deg,#1a1a1a,#222)}
.contact{position:absolute;top:40px;display:flex;gap:20px;color:#aaa;font-size:12px;line-height:18px}
.contact .icon{width:46px;height:46px;border-radius:50%;background:#6fb8e6;flex:none;display:flex;align-items:center;justify-content:center}
.contact.addr{left:164px}
.contact.phone{left:464px}
.contact.mail{left:764px}
.map-toggle{position:absolute;left:0;top:2174px;width:1200px;height:75px;background:var(--band);color:var(--white);text-align:center;font-size:13px;font-weight:500;padding-top:14px}
.map-toggle .plus{font-size:24px;line-height:22px;display:block}
.bottom-bar{position:absolute;left:0;top:2249px;width:1200px;height:66px;background:var(--dark)}
.copyright{position:absolute;left:160px;top:24px;color:#999;font-size:11px}
.social{position:absolute;right:160px;top:17px;display:flex;gap:8px}
.social span{width:32px;height:32px;border-radius:50%}
</style>
</head>
<body>

<section class="hero" role="img" aria-label="Sound engineer working at a mixing console in a warm-lit studio"></section>
<header class="site-header">
  <a class="brand" href="#">Vermilion Reel Works</a>
  <nav class="main-nav">
    <a class="active" href="#">HOME</a>
    <a href="#">ABOUT US</a>
    <a href="#">TEAM</a>
    <a href="#">SERVICES</a>
    <a href="#">FACILITY</a>
    <a href="#">JOB OPPORTUNITIES</a>
    <a href="#">CONTACT</a>
  </nav>
  <span class="lang">EN</span>
</header>
<div class="hero-copy">
  <svg width="40" height="36" viewBox="0 0 40 36" aria-hidden="true"><path d="M6 22V18a14 14 0 0 1 28 0v4" fill="none" stroke="#2bd4b0" stroke-width="3"/><rect x="3" y="20" width="8" height="13" rx="3" fill="#2bd4b0"/><rect x="29" y="20" width="8" height="13" rx="3" fill="#2bd4b0"/></svg>
  <h1 class="hero-title">Vermilion Reel Works</h1>
  <div class="divider"></div>
  <p class="hero-sub">Provides a well-designed working environment which amplifies<br>your team's ability to reach their creative goals.</p>
</div>

<section class="services">
  <div class="service-intro"><h2>Our Service</h2><div class="divider"></div></div>
  <article class="service-card" role="img" aria-label="Rack-mounted audio equipment"><div class="caption"><h3>Feature Films</h3><p>Sed ut perspiciatis unde omnis iste natus error doloremque laudantium,</p></div></article>
  <article class="service-card" role="img" aria-label="Mixing desk faders"><div class="caption"><h3>Music &amp; Scoring</h3><p>Sed ut perspiciatis unde omnis iste natus error doloremque laudantium,</p></div></article>
  <article class="service-card" role="img" aria-label="Audio interface front panel"><div class="caption"><h3>Commercials</h3><p>Sed ut perspiciatis unde omnis iste natus error doloremque laudantium,</p></div></article>
  <article class="service-card" role="img" aria-label="Preamp unit with glowing controls"><div class="caption"><h3>ADR &amp; Foley</h3><p>Sed ut perspiciatis unde omnis iste natus error doloremque laudantium,</p></div></article>
  <article class="service-card featured" role="img" aria-label="Control knobs with coloured buttons"><div class="caption"><h3>Sound &amp; Picture Editorial</h3><p>Sed ut perspiciatis unde omnis iste natus error doloremque laudantium,</p></div></article>
  <article class="service-card" role="img" aria-label="Studio monitor speaker"><div class="caption"><h3>Sound Design</h3><p>Sed ut perspiciatis unde omnis iste natus error doloremque laudantium,</p></div></article>
  <article class="service-card" role="img" aria-label="Control surface in a studio"><div class="caption"><h3>Video Game</h3><p>Sed ut perspiciatis unde omnis iste natus error doloremque laudantium,</p></div></article>
</section>

<section class="studio" role="img" aria-label="Darkened mixing console background">
  <div class="work">
    <h2>Work With Our Studio</h2>
    <div class="divider"></div>
    <div class="we-create">
      <div class="kicker">WE CREATE</div>
      <div class="big">Digital Experience</div>
      <div class="mid">for modern<br>digital world companies</div>
      <p>Lorem ipsum dolor sit amet, consectetur adipisicing elit, sed do eiusmod tempor incididunt ut labore et dolore magna aliqua.</p>
    </div>
    <a class="btn" href="#">FIND OUT HOW</a>
  </div>
  <div class="case">
    <h2>Vermilion Reel Works Case Study</h2>
    <div class="divider"></div>
    <div class="case-media" role="img" aria-label="Case study video still of golden packets in a glass">
      <svg width="62" height="62" viewBox="0 0 62 62" aria-hidden="true"><circle cx="31" cy="31" r="28" fill="none" stroke="#fff" stroke-width="4"/><path d="M25 19L44 31L25 43Z" fill="#fff"/></svg>
    </div>
    <p>Lorem ipsum dolor sit amet, consectetur adipisicing elit, sed do eiusmod tempor incididunt ut labore et dolore magna aliqua.</p>
  </div>
</section>

<section class="blog">
  <h2 class="blog-title">From The Blog</h2>
  <div class="divider"></div>
  <div class="blog-list">
    <article class="post"><div class="post-image" role="img" aria-label="Perforated speaker grille"><div class="date"><b>25</b><span>Jun</span></div></div><div class="day">Friday 2014</div><h3>Donec ultricies nunc rutrum</h3><p>Sed ut perspiciatis unde omnis iste natus error doloremque laudantium,</p></article>
    <article class="post"><div class="post-image" role="img" aria-label="Illuminated console buttons"><div class="date"><b>25</b><span>Jun</span></div></div><div class="day">Friday 2014</div><h3>Donec ultricies nunc rutrum</h3><p>Sed ut perspiciatis unde omnis iste natus error doloremque laudantium,</p></article>
    <article class="post"><div class="post-image" role="img" aria-label="Desk with control surface and keyboard"><div class="date"><b>25</b><span>Jun</span></div></div><div class="day">Friday 2014</div><h3>Donec ultricies nunc rutrum</h3><p>Sed ut perspiciatis unde omnis iste natus error doloremque laudantium,</p></article>
    <article class="post"><div class="post-image" role="img" aria-label="Stacked rack equipment"><div class="date"><b>25</b><span>Jun</span></div></div><div class="day">Friday 2014</div><h3>Donec ultricies nunc rutrum</h3><p>Sed ut perspiciatis unde omnis iste natus error doloremque laudantium,</p></article>
  </div>
</section>

<footer>
  <div class="footer-contacts">
    <div class="contact addr">
      <span class="icon"><svg width="22" height="22" viewBox="0 0 22 22" aria-hidden="true"><circle cx="11" cy="11" r="9" fill="none" stroke="#fff" stroke-width="2.5"/><circle cx="11" cy="11" r="3.5" fill="#fff"/></svg></span>
      <address style="font-style:normal">中国上海黄浦区青桐路58号<br>No.58 Qingtong Rd.<br>Shanghai China, 200023</address>
    </div>
    <div class="contact phone">
      <span class="icon"><svg width="22" height="22" viewBox="0 0 24 24" aria-hidden="true"><path d="M6.6 10.8a15 15 0 0 0 6.6 6.6l2.2-2.2c.3-.3.7-.4 1-.2 1.1.4 2.3.6 3.6.6.6 0 1 .4 1 1V20c0 .6-.4 1-1 1A17 17 0 0 1 3 4c0-.6.4-1 1-1h3.5c.6 0 1 .4 1 1 0 1.3.2 2.5.6 3.6.1.3 0 .7-.2 1z" fill="#fff"/></svg></span>
      <div>86 21 5550-1842<br>400-555-0178 (REEL)</div>
    </div>
    <div class="contact mail">
      <span class="icon"><svg width="22" height="16" viewBox="0 0 22 16" aria-hidden="true"><rect x="1" y="1" width="20" height="14" fill="none" stroke="#fff" stroke-width="2"/><path d="M1 1l10 8 10-8" fill="none" stroke="#fff" stroke-width="2"/></svg></span>
      <div>hello@vermilionreelworks.com</div>
    </div>
  </div>
  <div class="map-toggle"><span class="plus">+</span>SHOW THE MAP</div>
  <div class="bottom-bar">
    <p class="copyright">© 2014 Vermilion Reel Works</p>
    <div class="social" aria-label="Social links">
      <span style="background:#3ea6e6"></span>
      <span style="background:#3b5a9a"></span>
      <span style="background:#1f7fb5"></span>
      <span style="background:#d6483a"></span>
    </div>
  </div>
</footer>

</body>
</html>
```